Yacht Charter Broker needs a magazine page design

We are a travel agent for yachts called Velmoria Yacht Charters. www.velmoriacharters.example We are advertising in a magazine at the grand pacer equine fair - https://plgequinefair.example/ - and need a high-end luxury feeling magazine page.

Target Market(s)

Vacation goers looking to charter a crewed yacht.

Industry/Entity Type

Travel Agent

Requirements
Must have
• luxury feel. logo. website and social media icons if you feel necessary. Our motto is: Inhale. Exhale. Sail.
• Catamaran picture, snorkeling and other island, water looking pictures.
Nice to have
• Open to your design.
Should not have
• Nothing comes to mind.

```html
<!DOCTYPE html>
<html lang="en">
<head>
<meta charset="utf-8">
<title>Velmoria Yacht Charters – Magazine Page</title>
<link rel="stylesheet" href="https://fonts.googleapis.com/css2?family=Cormorant+Garamond:wght@500&family=Roboto+Condensed:wght@300;400&family=Raleway:wght@300;400&display=swap">
<style>
  :root {
    --backdrop: #efefed;
    --navy-deep: #121345;
    --navy: #1b1f60;
    --navy-light: #27307a;
    --sea-dark: #233680;
    --sea: #3a56a0;
    --sea-light: #6f87c2;
    --ink-light: #f4f5fa;
    --ink-soft: rgba(244, 245, 250, 0.82);
    --line-faint: rgba(244, 245, 250, 0.28);
  }
  * { margin: 0; padding: 0; box-sizing: border-box; }
  html, body {
    width: 680px;
    height: 1200px;
    overflow: hidden;
    background: var(--backdrop);
  }
  .magazine-page {
    position: absolute;
    left: 40px;
    top: 180px;
    width: 600px;
    height: 840px;
    background: radial-gradient(ellipse 75% 60% at 55% 42%, var(--navy-light) 0%, var(--navy) 55%, var(--navy-deep) 100%);
    color: var(--ink-light);
    overflow: hidden;
  }
  .brand-frame {
    position: absolute;
    left: 165px;
    top: 66px;
    width: 290px;
    height: 96px;
    border: 1px solid var(--ink-soft);
    text-align: center;
    padding-top: 19px;
  }
  .brand-name {
    font-family: "Cormorant Garamond", serif;
    font-weight: 500;
    font-size: 40px;
    letter-spacing: 6px;
    line-height: 1;
    color: var(--ink-light);
  }
  .brand-descriptor {
    font-family: "Cormorant Garamond", serif;
    font-weight: 500;
    font-size: 11px;
    letter-spacing: 3px;
    margin-top: 8px;
    color: var(--ink-soft);
  }
  .headline {
    position: absolute;
    left: 0;
    top: 186px;
    width: 100%;
    text-align: center;
    font-family: "Roboto Condensed", sans-serif;
    font-weight: 400;
    font-size: 24px;
    letter-spacing: 0.3px;
    color: var(--ink-light);
  }
  .hero-photo {
    position: absolute;
    left: 40px;
    top: 240px;
    width: 520px;
    height: 300px;
    border-radius: 4px;
    background: linear-gradient(155deg, var(--sea-dark) 0%, var(--sea) 45%, var(--sea-light) 62%, var(--sea) 78%, var(--sea-dark) 100%);
  }
  .sketch {
    position: absolute;
    width: 120px;
    height: 84px;
    border: 1px solid var(--line-faint);
    border-radius: 4px;
    background: linear-gradient(180deg, rgba(244,245,250,0.10) 0%, rgba(244,245,250,0.04) 100%);
  }
  .sketch--catamaran { left: 60px; top: 568px; }
  .sketch--sailboat { left: 220px; top: 600px; }
  .sketch--motor-yacht { left: 380px; top: 632px; width: 150px; }
  .motto {
    position: absolute;
    left: 60px;
    top: 728px;
    font-family: "Raleway", sans-serif;
    font-weight: 400;
    font-size: 28px;
    letter-spacing: 9px;
    color: var(--ink-light);
  }
  .website {
    position: absolute;
    left: 60px;
    top: 780px;
    font-family: "Raleway", sans-serif;
    font-weight: 400;
    font-size: 17px;
    letter-spacing: 4px;
    color: var(--ink-soft);
  }
</style>
</head>
<body>
  <main class="magazine-page">
    <div class="brand-frame">
      <div class="brand-name">VELMORIA</div>
      <div class="brand-descriptor">YACHT CHARTER BROKER</div>
    </div>
    <h1 class="headline">WE ARE THE LEADERS IN YACHT CHARTERING</h1>
    <div class="hero-photo" role="img" aria-label="Aerial photograph of a white motor yacht cutting through deep blue sea, leaving a wide foaming wake"></div>
    <div class="sketch sketch--catamaran" role="img" aria-label="Fine white line drawing of a catamaran under sail"></div>
    <div class="sketch sketch--sailboat" role="img" aria-label="Fine white line drawing of a sailboat"></div>
    <div class="sketch sketch--motor-yacht" role="img" aria-label="Fine white line drawing of a large motor yacht"></div>
    <p class="motto">INHALE. EXHALE. SAIL.</p>
    <p class="website">www.velmoriacharters.example</p>
  </main>
</body>
</html>
```